Billboard design for a small town Oral Surgeon

We are getting several billboards and need a design that highlights the doctors photo, and bullet points of what he does. Our business name is extremely long, so it’s a challenge to figure out how to do this. Maybe just use our logo? Open to ideas.
The logo can be shortened as designer sees fit, meaning we can drop the tag line. Important info to include:
Doctors name is Tobin Marek
The highlighted bullet points are:
•Implants
•wisdom teeth
•Jaw Surgery
•facial trauma
The goal of this billboard is to let our community know that they have an option here in Elda, our town. Many still drive to the city a couple hours away not knowing they now have an option here at home. Having a hard time finding examples of what I have in mind, so hoping this will get us going. I want it as “non-busy” as possible, so no unnecessary lines or anything that competes with the information we are trying to get across.

Target Market(s)

Everyone in town, just trying to spread the word that we are here

Industry/Entity Type

Medical/surgical (oral surgery)

Font styles to use
Sans Serif

Colors
0094D4
00A9DD
6FCCEA
C7EBF8
E9F6FB

Requirements
Must have
• *New note** Due to location of billboard, I prefer the photo of doctor to be on the left side. Must look neat and professional. Must highlight what we do.
Nice to have
• Our colors are a blue-green with silver, against black or white, but I’m flexible on this, I don’t necessarily need the colors highlighted. I’m also flexible on font style, just needs to be easy to read.
Should not have
• Distracting graphics, should not look like a dental office. That’s an issue we have is people thinking we are another dental office, we do not do any general dentistry, it’s surgery only.

```html
<!DOCTYPE html>
<html lang="en">
<head>
<meta charset="utf-8">
<title>Oral Surgery Billboard – Colour Options</title>
<link rel="stylesheet" href="https://fonts.googleapis.com/css2?family=Montserrat:wght@300;400;600;800&family=Open+Sans:wght@400;700&display=swap">
<style>
  :root {
    --ink: #000000;
    --silver: #808080;
    --blue: #4a7dff;
    --green: #11a004;
    --teal: #1a93a8;
    --white: #ffffff;
    --text-dark: #222222;
    --bg-aqua: #c1f8f2;
    --bg-mint: #d6fdd0;
    --bg-white: #ffffff;
  }
  * { box-sizing: border-box; margin: 0; padding: 0; }
  html, body { width: 1132px; height: 1200px; overflow: hidden; background: var(--white); }
  body { position: relative; font-family: "Montserrat", sans-serif; }

  .billboard {
    position: absolute;
    width: 827px;
    height: 297px;
    background: var(--board-bg);
    box-shadow: 2px 2px 3px rgba(0,0,0,0.45);
    overflow: hidden;
  }
  .billboard--aqua  { --board-bg: var(--bg-aqua);  left: 155px; top: 88px; }
  .billboard--mint  { --board-bg: var(--bg-mint);  left: 154px; top: 420px; }
  .billboard--white { --board-bg: var(--bg-white); left: 158px; top: 750px; }

  .doctor-photo {
    position: absolute; left: 0; top: 0;
    width: 202px; height: 246px;
    background: radial-gradient(ellipse at 50% 40%, #4a4a4e 0%, #2a2a2e 55%, #151518 100%);
  }
  .doctor-name {
    position: absolute; left: 0; top: 246px;
    width: 205px; height: 51px;
    background: var(--white);
    font-family: "Open Sans", sans-serif;
    font-size: 19px; line-height: 51px;
    text-align: center;
    color: #1a1a1a;
    white-space: nowrap;
  }
  .doctor-name b { font-weight: 700; letter-spacing: 0.5px; }

  .service {
    position: absolute; left: 202px;
    height: 50px;
    border-radius: 0 25px 25px 0;
    color: var(--white);
    font-weight: 800;
    font-size: 33px;
    letter-spacing: 2px;
    line-height: 50px;
    white-space: nowrap;
    text-align: right;
    padding-right: 18px;
  }
  .service--implants { top: 1px;   width: 243px; background: var(--ink); text-align: left; padding-left: 6px; }
  .service--wisdom   { top: 66px;  width: 310px; background: var(--silver); text-align: left; padding-left: 8px; }
  .service--jaw      { top: 131px; width: 354px; background: var(--blue); }
  .service--trauma   { top: 194px; width: 420px; background: var(--green); }

  .practice {
    position: absolute; left: 571px; top: 12px;
    width: 218px;
  }
  .practice-mark {
    width: 95px; height: 95px;
    margin: 0 0 12px 60px;
    border-radius: 50%;
    background: var(--teal);
  }
  .practice-name {
    font-weight: 300;
    font-size: 19px;
    line-height: 18px;
    color: var(--text-dark);
    text-transform: uppercase;
    letter-spacing: -0.3px;
  }

  .phone {
    position: absolute; left: 645px; top: 206px;
    font-weight: 800; font-size: 25px; letter-spacing: 2px;
    color: var(--ink);
  }

  .slogan {
    position: absolute; left: 204px; top: 257px;
    font-size: 26px; line-height: 30px;
    font-weight: 400; letter-spacing: 1.5px;
    color: var(--ink);
    white-space: nowrap;
  }
  .slogan strong { font-weight: 800; }
</style>
</head>
<body>

  <section class="billboard billboard--aqua">
    <div class="doctor-photo" role="img" aria-label="Portrait photo of Dr. Tobin Marek in suit and red tie"></div>
    <div class="doctor-name"><b>Dr, Tobin</b> Marek</div>
    <div class="service service--implants">• Implants</div>
    <div class="service service--wisdom">•Wisdom Teeth</div>
    <div class="service service--jaw">•Jaw Surgery</div>
    <div class="service service--trauma">•Facial Trauma</div>
    <div class="practice">
      <div class="practice-mark"></div>
      <p class="practice-name">Red River Oral &amp;<br>Facial Surgery</p>
    </div>
    <div class="phone">#81 33 333</div>
    <p class="slogan">WE <strong>DO SURGERY</strong> IN OUR <strong>TOWN ELDA</strong></p>
  </section>

  <section class="billboard billboard--mint">
    <div class="doctor-photo" role="img" aria-label="Portrait photo of Dr. Tobin Marek in suit and red tie"></div>
    <div class="doctor-name"><b>Dr, Tobin</b> Marek</div>
    <div class="service service--implants">• Implants</div>
    <div class="service service--wisdom">•Wisdom Teeth</div>
    <div class="service service--jaw">•Jaw Surgery</div>
    <div class="service service--trauma">•Facial Trauma</div>
    <div class="practice">
      <div class="practice-mark"></div>
      <p class="practice-name">Red River Oral &amp;<br>Facial Surgery</p>
    </div>
    <div class="phone">#81 33 333</div>
    <p class="slogan">WE <strong>DO SURGERY</strong> IN OUR <strong>TOWN ELDA</strong></p>
  </section>

  <section class="billboard billboard--white">
    <div class="doctor-photo" role="img" aria-label="Portrait photo of Dr. Tobin Marek in suit and red tie"></div>
    <div class="doctor-name"><b>Dr, Tobin</b> Marek</div>
    <div class="service service--implants">• Implants</div>
    <div class="service service--wisdom">•Wisdom Teeth</div>
    <div class="service service--jaw">•Jaw Surgery</div>
    <div class="service service--trauma">•Facial Trauma</div>
    <div class="practice">
      <div class="practice-mark"></div>
      <p class="practice-name">Red River Oral &amp;<br>Facial Surgery</p>
    </div>
    <div class="phone">#81 33 333</div>
    <p class="slogan">WE <strong>DO SURGERY</strong> IN OUR <strong>TOWN ELDA</strong></p>
  </section>

</body>
</html>
```